Quality Improvement Software for healthcare agencies needs a website.

Veltrix820 is a software for hospices and home health agencies to manage their Quality Assurance Performance Improvement programs to remain complaint with the standards set by Sanovia and the Bureau of Civic Wellbeing. The web accessible software-as-a-service provides an easy, turn-key way for agencies to organize all the information they need to manage and track.

Coded - Design and coding required

4 page

```html
<!DOCTYPE html>
<html lang="en">
<head>
<meta charset="utf-8">
<title>Veltrix820 — Healthcare Solution For Everyone</title>
<link href="https://fonts.googleapis.com/css2?family=DM+Sans:wght@400;500;700&family=Lora:wght@400;500&display=swap" rel="stylesheet">
<style>
:root{
  --ink:#1d1d2b;
  --body:#4a4a55;
  --muted:#8a8f98;
  --blue:#1f8ff0;
  --teal:#6fb3a2;
  --teal-soft:#e6f3ef;
  --ghost:#eef5ea;
  --line:#9ecbc0;
  --card-border:#d9dde2;
  --footer:#7ab6a8;
  --contact-left:#b9d6f2;
  --contact-right:#e3e8f9;
}
*{margin:0;padding:0;box-sizing:border-box}
html,body{width:1200px;height:5104px;overflow:hidden}
body{position:relative;background:#fff;font-family:"DM Sans",sans-serif;color:var(--ink)}
.abs{position:absolute}
.serif{font-family:"Lora",serif}
.ph{position:absolute;border-radius:8px}
/* header */
.site-header{position:absolute;top:0;left:0;width:1200px;height:100px;z-index:5}
.brand{position:absolute;left:174px;top:30px;display:flex;align-items:center;gap:10px;font-size:34px;font-weight:700;color:var(--ink)}
.brand .dot{width:26px;height:26px;background:var(--teal);border-radius:4px}
.nav{position:absolute;left:538px;top:38px;display:flex;gap:20px;font-size:14px;color:var(--ink)}
.search{position:absolute;left:1006px;top:36px}
/* hero */
.hero-bg{position:absolute;right:0;top:0;width:520px;height:570px;background:radial-gradient(ellipse at 100% 30%,#cfe9e5 0%,#e7f4f2 40%,rgba(255,255,255,0) 72%);z-index:0}
.hero-title{position:absolute;left:174px;top:166px;font-size:37px;font-weight:500;line-height:1.35;width:440px;z-index:2}
.hero-text{position:absolute;left:174px;top:272px;width:360px;font-size:13.5px;line-height:1.5;color:var(--body);z-index:2}
.btn{position:absolute;height:34px;padding:0 44px 0 20px;background:var(--blue);color:#fff;font-size:14px;font-weight:500;line-height:34px;z-index:2;white-space:nowrap}
.btn::after{content:"›";position:absolute;right:-14px;top:2px;width:30px;height:30px;border-radius:50%;background:var(--blue);border:3px solid #fff;box-shadow:0 0 0 1.5px var(--blue);font-size:20px;line-height:22px;text-align:center}
/* sections */
.ghost{position:absolute;font-family:"Lora",serif;font-size:62px;color:var(--ghost);white-space:nowrap}
.h2{position:absolute;font-size:24px;font-weight:500}
.para{position:absolute;font-family:"Lora",serif;font-size:11.5px;line-height:1.42;color:var(--body)}
.svc-card{position:absolute;width:176px;height:180px;border:1.5px solid var(--card-border);background:#fff;text-align:center;color:var(--teal);font-size:13.5px;line-height:1.45;padding:96px 10px 0}
.svc-card svg{position:absolute;left:56px;top:36px}
.checks{position:absolute;font-family:"Lora",serif;font-size:12px;color:var(--ink)}
.checks span{position:absolute;white-space:nowrap;padding-left:24px}
.checks span::before{content:"✓";position:absolute;left:0;top:-2px;width:14px;height:14px;border:1.5px solid var(--teal);border-radius:50%;font-size:9px;color:var(--teal);text-align:center;line-height:12px}
.stat{position:absolute;width:150px;height:150px;border-radius:50%;border:2px dashed var(--line);text-align:center;background:#fff}
.stat .num{position:absolute;left:0;right:0;top:72px;font-size:30px;color:#e1e4e6;font-weight:500}
.stat .lbl{position:absolute;left:0;right:0;top:80px;font-size:12px;color:#555}
.stat svg{position:absolute;left:56px;top:28px}
.seo{position:absolute;left:174px;top:2745px;width:855px;height:225px;background:#eef4ee;border:1.5px solid #c9d9cd}
.seo-input{position:absolute;left:166px;top:140px;width:520px;height:52px;background:#fff;border:1.5px solid #cfd6d2;font-size:12px;color:#666;padding:18px 32px}
.news{position:absolute;top:3178px;width:268px;height:345px}
.news .img{position:absolute;left:0;top:0;width:268px;height:272px}
.news .meta{position:absolute;left:16px;top:272px;width:236px;height:72px;background:#fff;border:1.5px solid #dfe3e6;padding:10px 12px;font-size:13px;line-height:1.4}
.news .by{display:flex;justify-content:space-between;font-size:9px;color:#555;margin-bottom:10px}
.avatar{position:absolute;border-radius:50%}
.form-box{position:absolute;left:577px;top:4175px;width:452px;height:422px;background:#fff;border:1.5px solid #d5dae8}
.field{position:absolute;font-size:11px;color:#555;border-bottom:1.5px solid #cfd3de;height:34px}
.footer{position:absolute;left:0;top:4650px;width:1200px;height:454px;background:var(--footer);color:#fff}
.footer h4{position:absolute;font-size:17px;font-weight:500}
.footer ul{position:absolute;list-style:none;font-family:"Lora",serif;font-size:11px;line-height:35px}
.social{position:absolute;left:174px;top:4995px;width:855px;height:62px;display:flex;border:1.5px solid rgba(255,255,255,.45);color:#fff}
.social div{flex:1;border-right:1.5px solid rgba(255,255,255,.45);display:flex;align-items:center;justify-content:center;font-family:"Lora",serif;font-size:13px;gap:8px}
.social div:last-child{border-right:0}
.social i{width:10px;height:10px;border:1.5px solid #fff;border-radius:50%}
</style>
</head>
<body>

<div class="hero-bg"></div>

<header class="site-header">
  <div class="brand"><span class="dot"></span>Veltrix820</div>
  <nav class="nav"><span>Home</span><span>Pages</span><span>Our Services</span><span>Blog</span><span>Portfolio</span><span>Contact Us</span></nav>
  <svg class="search" width="20" height="20" viewBox="0 0 20 20"><circle cx="8" cy="8" r="6" fill="none" stroke="#333" stroke-width="1.6"/><line x1="12.5" y1="12.5" x2="18" y2="18" stroke="#333" stroke-width="1.6"/></svg>
</header>

<section class="hero">
  <h1 class="hero-title">Healthcare Solution For Everyone</h1>
  <p class="hero-text serif">It is a long established fact that a reader will be distracted by the readable content of a page when looking at its layout.</p>
  <a class="btn" style="left:174px;top:366px">Contact us</a>
  <div class="ph" role="img" aria-label="Isometric illustration of a clinic platform with doctors, patients, medicine boxes and a stethoscope" style="left:560px;top:175px;width:560px;height:310px;background:radial-gradient(ellipse at 45% 60%,#cdeedb 0%,#e4f3ef 45%,rgba(255,255,255,0) 72%);border-radius:50%;z-index:1"></div>
</section>

<section class="about">
  <div class="ph" role="img" aria-label="Illustration of medical staff around a large phone showing health charts" style="left:174px;top:570px;width:416px;height:350px;background:radial-gradient(circle at 50% 45%,#eef1fa 0%,#f3f6f9 60%,#fbfcfd 100%);border-radius:200px 200px 10px 10px"></div>
  <div class="ghost" style="left:620px;top:640px">About us</div>
  <h2 class="h2" style="left:628px;top:680px">Who We Are?</h2>
  <p class="para" style="left:628px;top:728px;width:400px">The Point Of Using Lorem Ipsum Is That It Has A More-Or-Less Normal Distribution Of Letters, As Opposed To Using 'Content Here, Content Here', Making It Look Like Readable English. Many Desktop Publishing Packages And Web Page Editors Now Use Lorem Ipsum As Their Default Model Text, And A Search For 'lorem Ipsum' Will Uncover Many Web Sites Still In Their Infancy. Various Versions Have Evolved Over The Years, Sometimes By Accident, Sometimes On Purpose (Injected Humour And The Like).</p>
  <a class="btn" style="left:628px;top:880px">Know More</a>
</section>

<svg class="abs" style="left:0;top:0" width="1200" height="1800">
  <path d="M440 932 C430 1010,560 1020,680 1030 C780 1038,810 1060,812 1090" fill="none" stroke="var(--line)" stroke-width="2" stroke-dasharray="6 6"/>
  <circle cx="440" cy="932" r="5" fill="var(--line)"/><path d="M806 1088 l6 8 l6 -8z" fill="var(--line)"/>
  <path d="M810 1560 C812 1640,640 1640,540 1660 C470 1675,440 1690,440 1718" fill="none" stroke="var(--line)" stroke-width="2" stroke-dasharray="6 6"/>
  <circle cx="810" cy="1560" r="5" fill="var(--line)"/><path d="M434 1716 l6 8 l6 -8z" fill="var(--line)"/>
</svg>

<section class="services">
  <div class="ghost" style="left:174px;top:1048px">Services</div>
  <h2 class="h2" style="left:188px;top:1090px">Deserves Our Best Services</h2>
  <p class="para" style="left:188px;top:1140px;width:380px">The Point Of Using Lorem Ipsum Is That It Has A More-Or-Less Normal Distribution Of Letters.</p>
  <a class="btn" style="left:174px;top:1206px">View All</a>
  <div class="svc-card" style="left:174px;top:1260px">
    <svg width="64" height="50" viewBox="0 0 64 50" fill="none" stroke="var(--teal)" stroke-width="2"><rect x="4" y="12" width="36" height="26"/><path d="M40 20h12l8 10v8H40z"/><circle cx="16" cy="42" r="5"/><circle cx="48" cy="42" r="5"/><path d="M22 18v14M15 25h14"/></svg>
    Improving response for emergency</div>
  <div class="svc-card" style="left:356px;top:1355px">
    <svg width="64" height="56" viewBox="0 0 64 56" fill="none" stroke="var(--teal)" stroke-width="2"><rect x="14" y="4" width="36" height="40" rx="4"/><circle cx="32" cy="24" r="10"/><path d="M32 19v10M27 24h10M6 52h52"/></svg>
    Looking to elevate senior care &amp; aging that are in place</div>
  <div class="svc-card" style="left:174px;top:1450px">
    <svg width="64" height="56" viewBox="0 0 64 56" fill="none" stroke="var(--teal)" stroke-width="2"><rect x="10" y="4" width="44" height="34"/><path d="M26 16v12M20 22h12M4 50h56M22 38v12M42 38v12"/></svg>
    Restructure patient treatment at the hospital</div>
  <div class="ph" role="img" aria-label="Illustration of a doctor and patient beside a large monitor with medical icons and plants" style="left:580px;top:1125px;width:440px;height:395px;background:radial-gradient(circle at 50% 45%,#ece8fb 0%,#f3f1fc 55%,#fbfbfe 100%);border-radius:200px 200px 20px 20px"></div>
</section>

<section class="why">
  <div class="ph" role="img" aria-label="Illustration of a doctor and patient in front of a laptop showing health data" style="left:174px;top:1755px;width:416px;height:355px;background:radial-gradient(circle at 45% 45%,#eef1fa 0%,#f3f6f9 60%,#fbfcfd 100%);border-radius:200px 200px 10px 10px"></div>
  <div class="ghost" style="left:614px;top:1808px">Information</div>
  <h2 class="h2" style="left:628px;top:1846px">Why Choose Us?</h2>
  <p class="para" style="left:628px;top:1896px;width:400px">The Point Of Using Lorem Ipsum Is That It Has A More-Or-Less Normal Distribution Of Letters, As Opposed To Using 'Content Here, Content Here', Making It Look Like Readable English.</p>
  <div class="checks" style="left:628px;top:1964px">
    <span style="left:0;top:0">Expert Team Member</span>
    <span style="left:218px;top:0">Time Management</span>
    <span style="left:0;top:36px">Work Dedication</span>
    <span style="left:218px;top:36px">Faster Enrollments</span>
  </div>
  <a class="btn" style="left:628px;top:2048px">Explore More</a>
</section>

<section class="achievements">
  <div class="ghost" style="left:0;width:1200px;text-align:center;top:2262px">Achievements</div>
  <h2 class="h2" style="left:0;width:1200px;text-align:center;top:2300px">Clients Reviews</h2>
  <p class="para" style="left:300px;width:600px;text-align:center;top:2344px">All the Lorem Ipsum generators on the Internet tend to repeat predefined chunks as necessary, making this the first true generator on the Internet.</p>
  <svg class="abs" style="left:0;top:2400px" width="1200" height="300">
    <path d="M312 150 C360 170,380 200,412 200" fill="none" stroke="var(--line)" stroke-width="2" stroke-dasharray="6 6"/>
    <path d="M560 190 C600 170,610 140,642 112" fill="none" stroke="var(--line)" stroke-width="2" stroke-dasharray="6 6"/>
    <path d="M790 90 C830 90,860 110,884 130" fill="none" stroke="var(--line)" stroke-width="2" stroke-dasharray="6 6"/>
  </svg>
  <div class="stat" style="left:175px;top:2430px"><svg width="40" height="36" viewBox="0 0 40 36" fill="var(--blue)"><circle cx="20" cy="10" r="6"/><circle cx="8" cy="13" r="4"/><circle cx="32" cy="13" r="4"/><path d="M10 30c0-7 4-12 10-12s10 5 10 12zM0 30c0-6 3-9 8-9v9zM40 30c0-6-3-9-8-9v9z"/></svg><div class="num">680</div><div class="lbl">Happy Clients</div></div>
  <div class="stat" style="left:410px;top:2515px"><svg width="40" height="36" viewBox="0 0 40 36" fill="var(--blue)"><path d="M2 12l10-6 8 6 8-6 10 6-18 16z"/></svg><div class="num">458</div><div class="lbl">Trusted Users</div></div>
  <div class="stat" style="left:641px;top:2425px"><svg width="40" height="36" viewBox="0 0 40 36" fill="none" stroke="var(--blue)" stroke-width="3"><circle cx="18" cy="18" r="12"/><path d="M12 18l5 5 8-9"/></svg><div class="num">298</div><div class="lbl">Projects</div></div>
  <div class="stat" style="left:875px;top:2520px"><svg width="40" height="36" viewBox="0 0 40 36" fill="var(--blue)"><circle cx="20" cy="14" r="11"/><path d="M12 22l-4 14 12-6 12 6-4-14z"/></svg><div class="num">50</div><div class="lbl">Awards</div></div>
</section>

<section class="seo">
  <h2 style="position:absolute;left:0;right:0;top:38px;text-align:center;font-size:24px;font-weight:500">Check your Website's SEO!</h2>
  <p class="para" style="left:140px;width:575px;text-align:center;top:80px">All the Lorem Ipsum generators on the Internet tend to repeat predefined chunks as necessary, making this the first true generator on the Internet.</p>
  <div class="seo-input">Email
    <svg style="position:absolute;right:30px;top:14px" width="22" height="22" viewBox="0 0 22 22"><path d="M2 10L20 2 13 20 10 12z" fill="none" stroke="var(--teal)" stroke-width="2"/></svg></div>
</section>
<div class="ph" role="img" aria-label="Line illustration of a rocket launching from clouds" style="left:900px;top:2760px;width:180px;height:240px;background:radial-gradient(ellipse at 50% 75%,#f0f3f5 0%,rgba(245,247,248,.5) 55%,rgba(255,255,255,0) 80%)"></div>

<section class="blog">
  <div class="ghost" style="left:174px;top:3062px">Blog</div>
  <h2 class="h2" style="left:186px;top:3110px">Latest News</h2>
  <a class="btn" style="left:894px;top:3090px">View All</a>
  <article class="news" style="left:174px">
    <div class="img" role="img" aria-label="Isometric illustration of a doctor at a digital medical interface" style="background:linear-gradient(135deg,#f0517e,#d22966)"></div>
    <div class="meta"><div class="by"><span>● Dana Whitlow</span><span>April 30, 2023</span></div>Lorem Ipsum available, but the majority have suffered alteration</div>
  </article>
  <article class="news" style="left:467px">
    <div class="img" role="img" aria-label="Illustration of a laptop showing a health information video" style="background:linear-gradient(135deg,#3a7ff0,#7fb3f8)"></div>
    <div class="meta"><div class="by"><span>● Dana Whitlow</span><span>April 30, 2023</span></div>Lorem Ipsum available, but the majority have suffered alteration</div>
  </article>
  <article class="news" style="left:760px">
    <div class="img" role="img" aria-label="Illustration of a family consulting a doctor on a large phone" style="background:linear-gradient(135deg,#eef3fb,#cfe3f3)"></div>
    <div class="meta"><div class="by"><span>● Dana Whitlow</span><span>April 30, 2023</span></div>Lorem Ipsum available, but the majority have suffered alteration</div>
  </article>
</section>

<section class="testimonial">
  <div class="ph" role="img" aria-label="Faint dotted world map" style="left:300px;top:3640px;width:600px;height:260px;background:radial-gradient(ellipse,#f6f7f8 0%,rgba(255,255,255,0) 70%)"></div>
  <div class="avatar" role="img" aria-label="Client portrait" style="left:174px;top:3686px;width:138px;height:138px;background:#d9888f"></div>
  <div class="avatar" role="img" aria-label="Client portrait" style="left:496px;top:3705px;width:82px;height:82px;background:#4f9a72"></div>
  <div class="avatar" role="img" aria-label="Client portrait" style="left:770px;top:3640px;width:134px;height:134px;background:#e78b52"></div>
  <div class="avatar" role="img" aria-label="Client portrait" style="left:664px;top:3772px;width:56px;height:56px;background:#d9c3b0"></div>
  <div class="avatar" role="img" aria-label="Client portrait" style="left:360px;top:3836px;width:58px;height:58px;background:#7fc3c9"></div>
  <div class="avatar" role="img" aria-label="Client portrait" style="left:944px;top:3774px;width:82px;height:82px;background:#3e72e8"></div>
  <div style="position:absolute;left:0;right:0;top:3910px;text-align:center;font-size:17px">Testimonial</div>
  <p class="serif" style="position:absolute;left:330px;width:540px;top:3960px;text-align:center;font-size:25px;line-height:1.3;color:#333"><span style="color:var(--teal)">❝</span> I was very impressed by Norvane service lorem ipsum impressed by the Norvane service lorem ipsum is simply free text <span style="color:var(--teal)">❞</span></p>
</section>

<section class="contact">
  <div class="abs" style="left:0;top:4118px;width:420px;height:532px;background:var(--contact-left)"></div>
  <div class="abs" style="left:420px;top:4118px;width:780px;height:532px;background:var(--contact-right)"></div>
  <div class="ph" role="img" aria-label="Isometric illustration of a laptop with medical records, test tubes and a tooth model" style="left:40px;top:4290px;width:480px;height:300px;background:radial-gradient(ellipse at 50% 50%,#d6e5f7 0%,rgba(214,229,247,.5) 55%,rgba(214,229,247,0) 75%);border-radius:50%"></div>
  <div class="form-box">
    <h3 class="serif" style="position:absolute;left:0;right:0;top:48px;text-align:center;font-size:17px;font-weight:500;letter-spacing:.5px">GET IN TOUCH</h3>
    <div class="field" style="left:20px;top:106px;width:200px">Name</div>
    <div class="field" style="left:232px;top:106px;width:200px">Phone</div>
    <div class="field" style="left:20px;top:178px;width:412px">Email</div>
    <div class="field" style="left:20px;top:252px;width:412px;border:0">Message</div>
    <a class="btn" style="left:114px;top:358px">Make A Reservation</a>
  </div>
</section>

<footer class="footer">
  <div class="brand" style="top:102px;color:#fff;font-size:38px"><span class="dot" style="background:#fff"></span>Veltrix820</div>
  <p class="serif" style="position:absolute;left:174px;top:164px;width:250px;font-size:10.5px;line-height:1.45">Contrary to popular belief, Lorem Ipsum is not simply random text. It has roots in a piece of classical Latin literature from 45 BC, making it over 2000 years old.</p>
  <div style="position:absolute;left:174px;top:228px;font-size:18px">+(555) 010-2384</div>
  <h4 style="left:622px;top:88px">Our Services</h4>
  <ul style="left:622px;top:120px"><li>Senior Citizen Care</li><li>Health &amp; Medical</li><li>Medical Checkup</li><li>Nursing Care</li><li>Residential Care</li><li>Personalized Care</li></ul>
  <h4 style="left:932px;top:88px">Quick Link</h4>
  <ul style="left:932px;top:120px"><li>About Company</li><li>Team Members</li><li>Privacy Policy</li><li>Recent Articles</li><li>Testimonials</li><li>Contact Us</li></ul>
  <div style="position:absolute;left:0;right:0;top:425px;text-align:center;font-family:'Lora',serif;font-size:11px">© Copyright 2023. All rights reserved. Veltrix820</div>
</footer>
<div class="social">
  <div><i></i>Chatterly</div><div><i></i>Postwave</div><div><i></i>Linkwise</div><div><i></i>Snapframe</div><div><i></i>Vidstream</div>
</div>

</body>
</html>
```